Whitmore Business Card Design

The name of the business is Dara Whitmore, CPA LLC
The service that we offer is Accounting, Tax & Consulting Services. I need it to have the following items:
Dara Whitmore, Principal
Phone Number
Email Address
Physical Address

I have attached the company logo, one in black and one in white. Please provide a design in black background and the other in white background. Please include "Accounting, Tax & Consulting Services". I want the business card to be clean and very professional.

```html
<!DOCTYPE html>
<html lang="en">
<head>
<meta charset="utf-8">
<title>Dara Whitmore, CPA LLC — Business Cards</title>
<link rel="stylesheet" href="https://fonts.googleapis.com/css2?family=Montserrat:wght@400;500;600&family=Open+Sans:wght@300;400&display=swap">
<style>
  :root {
    --backdrop: #d9dadb;
    --card-black: #000000;
    --bar-grey: #38383a;
    --brand-red: #a5171c;
    --brand-grey: #8a8a8d;
    --text-white: #ffffff;
    --text-soft: #c9c9cb;
    --text-dim: #9a9a9d;
  }
  * { margin: 0; padding: 0; box-sizing: border-box; }
  html, body { width: 1200px; height: 800px; overflow: hidden; }
  body { background: var(--backdrop); position: relative; font-family: "Open Sans", Arial, sans-serif; }

  .card {
    position: absolute;
    width: 440px;
    height: 274px;
    background: var(--card-black);
    overflow: hidden;
    box-shadow: 0 3px 8px rgba(0,0,0,0.25);
  }
  .card--front { left: 193px; top: 101px; }
  .card--back  { left: 567px; top: 424px; }

  /* brand lockup */
  .brand { position: absolute; display: flex; align-items: center; }
  .brand__square { background: var(--brand-red); flex: none; }
  .brand__text { display: flex; flex-direction: column; font-family: "Montserrat", Arial, sans-serif; }
  .brand__name { color: var(--brand-grey); font-weight: 500; text-transform: uppercase; white-space: nowrap; }
  .brand__tagline { color: var(--text-soft); font-weight: 600; text-transform: uppercase; white-space: nowrap; }

  .card--front .brand { left: 34px; top: 48px; gap: 8px; }
  .card--front .brand__square { width: 22px; height: 22px; }
  .card--front .brand__name { font-size: 11px; letter-spacing: 0.2px; line-height: 13px; }
  .card--front .brand__tagline { font-size: 7.4px; letter-spacing: 1px; line-height: 10px; }

  .card--back .brand { left: 70px; top: 108px; gap: 14px; }
  .card--back .brand__square { width: 36px; height: 36px; }
  .card--back .brand__name { font-size: 17px; letter-spacing: 0.3px; line-height: 19px; }
  .card--back .brand__tagline { font-size: 12px; letter-spacing: 1.6px; line-height: 17px; }

  /* contact block */
  .contact { position: absolute; left: 33px; color: var(--text-white); font-size: 7.8px; line-height: 14px; list-style: none; }
  .contact--address { top: 121px; }
  .contact--reach { top: 171px; }

  .person { position: absolute; left: 263px; top: 170px; }
  .person__name { color: var(--text-white); font-size: 15.5px; font-weight: 400; letter-spacing: 1px; line-height: 20px; }
  .person__rule { width: 19px; height: 1px; background: var(--brand-red); margin: 2px 0 5px; }
  .person__role { color: var(--text-dim); font-size: 10px; letter-spacing: 1px; line-height: 12px; }

  /* bottom bands */
  .band { position: absolute; bottom: 0; background: var(--bar-grey); }
  .accent { position: absolute; bottom: 0; background: var(--brand-red); }

  .card--front .band { left: 0; width: 399px; height: 11px; }
  .card--front .accent { right: 0; width: 13px; height: 11px; }
  .services-strip {
    position: absolute; left: 33px; bottom: 1px;
    color: var(--text-white); font-family: "Montserrat", Arial, sans-serif;
    font-size: 5.4px; font-weight: 500; letter-spacing: 0.4px; line-height: 9px; text-transform: uppercase;
  }

  .card--back .band { left: 34px; right: 0; height: 15px; }
  .card--back .accent { left: 0; width: 13px; height: 15px; }

  .divider { position: absolute; left: 64px; top: 152px; width: 309px; height: 1px; background: var(--text-soft); }
  .services {
    position: absolute; left: 64px; top: 157px; width: 309px; text-align: center;
    color: var(--text-soft); font-family: "Montserrat", Arial, sans-serif;
    font-size: 8.6px; letter-spacing: 3.2px; line-height: 12px; text-transform: uppercase; white-space: nowrap;
  }
</style>
</head>
<body>

  <section class="card card--front" aria-label="Business card front">
    <div class="brand">
      <span class="brand__square"></span>
      <div class="brand__text">
        <span class="brand__name">Dara Whitmore, CPA, LLC</span>
        <span class="brand__tagline">Certified Public Accountant</span>
      </div>
    </div>

    <ul class="contact contact--address">
      <li>Company address line 1</li>
      <li>Address line 2</li>
    </ul>
    <ul class="contact contact--reach">
      <li>+12 345 678 90</li>
      <li>email@yourcompany.com</li>
      <li>www.company.com</li>
    </ul>

    <div class="person">
      <h1 class="person__name">DARA WHITMORE</h1>
      <div class="person__rule"></div>
      <p class="person__role">PRINCIPAL</p>
    </div>

    <div class="band"></div>
    <p class="services-strip">Accounting | Tax | Consulting Services</p>
    <div class="accent"></div>
  </section>

  <section class="card card--back" aria-label="Business card back">
    <div class="brand">
      <span class="brand__square"></span>
      <div class="brand__text">
        <span class="brand__name">Dara Whitmore, CPA, LLC</span>
        <span class="brand__tagline">Certified Public Accountant</span>
      </div>
    </div>
    <div class="divider"></div>
    <p class="services">Accounting | Tax | Consulting Services</p>

    <div class="accent"></div>
    <div class="band"></div>
  </section>

</body>
</html>
```